Stylish, Masculine Design - Men's Clothing

Brightmore Garment Depot is a 14,000 square foot warehouse outlet store open to the public since 2005. 50+ brands. Well-known designer brand names and private labels. 30-80% off retail everyday. Lowest prices guaranteed. Average suit price $150. Average shirt price $20. One-stop shop shopping. Men's suits, tuxedos, tuxedo rentals, dress shirts, ties, dress shoes, boy's suits and tuxedos, clergy robes, clergy shirts, cologne, loungewear. Slim fits (Prom Dance), business styles, "church" fashion, security-related uniform. Alterations done by expert tailors on premises for an extra charge.
The final design for both business card and logo should portray stylishness and masculinity.
Updates
We will be changing our name. Details below.New name: Warehouse Suit & TuxFormer name: Brightmore Garment Depot Added Monday, December 26, 2016
Target Market(s)
Gender: 80% Male, 15% Female, 5% Transgender
Location: 80% 10 Mile Radius, 20% >10 Mile Radius
Age: 17-18 (Primarily prom), 18-35 (Primarily Interviews and Weddings), 36-70 (primarily Church and events)
Race: African-American 50%, Latino-American 20%, White 15%, 10% Asian 5% Other
Religions: Christian 50%, 20% Catholic, 10% Mormon, 20% Other/None
Occupation: Local government 40%, Large corporation employee 20%, Small business employee 10%, Small business owner 10%, 20% Unemployed (high school, college)
Education: High School or equivalent 40%, College 30%, Some College 20%, Masters/Doctors 10%
Industry/Entity Type
Retail
Contact Information for Business Card
Name: Peter Galloway
Title: Sales Associate
Address: 517 E. Corvina Ave. Gardena, CA 90251
Phone Number: 310.586.2043
Slogan: Warehouse Selection. Outlet Prices, Outstanding Service
www.brightmoregarmentdepot-example.com
Logo Text
BGD (Acronym for Brightmore Garment Depot) or Image
Requirements
Must have
- Easy to read
- Visually appealing

```html
<!DOCTYPE html>
<html lang="en">
<head>
<meta charset="utf-8">
<title>Brightmore Garment Depot — Business Card</title>
<link href="https://fonts.googleapis.com/css2?family=Open+Sans:wght@300;400;600;700;800&display=swap" rel="stylesheet">
<style>
  :root {
    --stage: #e6e4e1;
    --card-black: #1c1c1c;
    --card-black-light: #3a3a3a;
    --card-white: #fbfbfb;
    --ink: #262626;
    --ink-soft: #6b6b6b;
    --ink-faint: #9a9a9a;
    --accent-red: #d2263f;
    --accent-red-light: #e4546b;
    --white: #ffffff;
  }
  * { box-sizing: border-box; margin: 0; padding: 0; }
  html, body { width: 1200px; height: 1062px; overflow: hidden; }
  body {
    background: var(--stage);
    font-family: "Open Sans", Arial, sans-serif;
    position: relative;
  }
  .card {
    position: absolute;
    left: 180px;
    width: 840px;
    height: 480px;
    border-radius: 6px;
    box-shadow: 0 8px 24px rgba(0,0,0,0.18);
    overflow: hidden;
  }
  /* Front */
  .card-front {
    top: 30px;
    background: linear-gradient(120deg, var(--card-black) 0%, var(--card-black-light) 48%, var(--card-black) 100%);
  }
  .front-artwork {
    position: absolute;
    left: 90px;
    top: 110px;
    width: 300px;
    height: 260px;
    border-radius: 4px;
    background: linear-gradient(150deg, var(--white) 0%, #d9d9d9 30%, var(--accent-red-light) 55%, var(--accent-red) 100%);
    opacity: 0.9;
  }
  .front-brand {
    position: absolute;
    right: 50px;
    top: 195px;
    width: 360px;
  }
  .front-brand .rule {
    height: 2px;
    width: 120px;
    margin-left: auto;
    background: var(--accent-red);
    margin-bottom: 10px;
  }
  .front-brand .brand-name {
    color: var(--white);
    font-weight: 700;
    font-size: 26px;
    line-height: 1.2;
    white-space: nowrap;
  }
  .front-brand .slogan {
    color: #bdbdbd;
    font-size: 11px;
    margin-top: 8px;
    letter-spacing: 0.2px;
    white-space: nowrap;
  }
  /* Back */
  .card-back {
    top: 552px;
    background: linear-gradient(135deg, var(--white) 0%, var(--card-white) 60%, #ececec 100%);
    border-right: 10px solid var(--card-black);
  }
  .back-brand {
    position: absolute;
    right: 50px;
    top: 70px;
    width: 520px;
  }
  .back-brand .brand-name {
    color: var(--ink);
    font-weight: 700;
    font-size: 40px;
    line-height: 1.1;
    white-space: nowrap;
    text-align: right;
  }
  .back-brand .rule {
    height: 3px;
    width: 190px;
    margin: 12px 0 0 auto;
    background: var(--accent-red);
  }
  .back-brand .slogan {
    color: var(--ink-faint);
    font-size: 13px;
    margin-top: 10px;
    letter-spacing: 0.3px;
    text-align: right;
    white-space: nowrap;
  }
  .holder {
    position: absolute;
    left: 60px;
    top: 70px;
  }
  .holder .name {
    font-weight: 800;
    font-size: 21px;
    color: var(--ink);
  }
  .holder .title {
    font-weight: 400;
    font-size: 18px;
    color: var(--ink);
    margin-top: 2px;
  }
  .divider {
    position: absolute;
    left: 60px;
    top: 225px;
    width: 80px;
    height: 2px;
    background: linear-gradient(90deg, transparent, #8a8a8a, transparent);
  }
  .contacts {
    position: absolute;
    left: 60px;
    top: 270px;
    list-style: none;
  }
  .contacts li {
    display: flex;
    align-items: center;
    gap: 12px;
    height: 34px;
    font-size: 18px;
    color: var(--ink);
    font-weight: 400;
  }
  .contacts svg {
    width: 22px;
    height: 22px;
    flex: none;
  }
</style>
</head>
<body>

<section class="card card-front">
  <div class="front-artwork" role="img" aria-label="White bow tie and red necktie illustration"></div>
  <div class="front-brand">
    <div class="rule"></div>
    <div class="brand-name">Brightmore Garment Depot</div>
    <div class="slogan">Wide Selection. Fair Prices. Friendly Service</div>
  </div>
</section>

<section class="card card-back">
  <div class="holder">
    <div class="name">Add name</div>
    <div class="title">President</div>
  </div>
  <div class="divider"></div>
  <ul class="contacts">
    <li>
      <svg viewBox="0 0 22 22" aria-hidden="true"><rect width="22" height="22" rx="3" fill="#333"/><path d="M7 5h3l1 4-2 1a7 7 0 0 0 3 3l1-2 4 1v3a2 2 0 0 1-2 2A11 11 0 0 1 5 7a2 2 0 0 1 2-2z" fill="#fff"/></svg>
      123-456-7890
    </li>
    <li>
      <svg viewBox="0 0 22 22" aria-hidden="true"><rect width="22" height="22" rx="3" fill="#333"/><rect x="5" y="6" width="12" height="10" rx="1" fill="none" stroke="#fff" stroke-width="1.6"/><rect x="8" y="9" width="6" height="3" fill="#fff"/></svg>
      123-456-7890
    </li>
    <li>
      <svg viewBox="0 0 22 22" aria-hidden="true"><rect width="22" height="22" rx="3" fill="#333"/><circle cx="11" cy="11" r="6" fill="none" stroke="#fff" stroke-width="1.4"/><path d="M5 11h12M11 5v12M7 7.5h8M7 14.5h8" stroke="#fff" stroke-width="1"/></svg>
      www.cardholder-example.com
    </li>
    <li>
      <svg viewBox="0 0 22 22" aria-hidden="true"><rect width="22" height="22" rx="3" fill="#333"/><text x="11" y="16" text-anchor="middle" font-family="Open Sans, sans-serif" font-size="14" font-weight="700" fill="#fff">@</text></svg>
      info@cardholder-example.com
    </li>
  </ul>
  <div class="back-brand">
    <div class="brand-name">Brightmore Garment Depot</div>
    <div class="rule"></div>
    <div class="slogan">Wide Selection. Fair Prices. Friendly Service</div>
  </div>
</section>

</body>
</html>
```